Business Card Design Project

I need a business card design for an Organic drive thru coffee kiosk. We will serve organic coffee, teas & smoothies and will serve healthy breakfast food/snacks for people on the go.
I want the card to have 2-3 colors max (earthy colors like browns, greens and so on).
I have attached the logo I want used and would love to play off the theme of "balance."
Include:
Tidy-Kettle Coffee
address: 4820 Gorvin Ct. Raleigh, NC 27583
phone: 919-731-4062
website: www.tidy-kettle.com (website is not up yet but still include it on card)
email: Rosalind@tidy-kettle.com
I want one of the following sayings somewhere on the card (the front or back is fine):
"Eat & Drink Well, on the run!"
"Break the fast with Tidy-Kettle"
Maybe on the back list what we offer:
-Organic coffee, espresso & tea
-Blendora smoothies & protein shakes
-Zesty Pour (100% fresh local fruit and veggies)
-Tender Nibs

```html
<!DOCTYPE html>
<html lang="en">
<head>
<meta charset="utf-8">
<title>Tidy-Kettle Organic Coffee + Cafe — Card</title>
<link href="https://fonts.googleapis.com/css2?family=PT+Sans:wght@400&display=swap" rel="stylesheet">
<style>
  :root {
    --paper: #ffffff;
    --espresso: #3a1a10;
    --roast: #7a2a1c;
  }
  * { margin: 0; padding: 0; box-sizing: border-box; }
  html, body {
    width: 1200px;
    height: 687px;
    overflow: hidden;
    background: var(--paper);
  }
  .card {
    position: relative;
    width: 1200px;
    height: 687px;
    background: var(--paper);
    font-family: "PT Sans", "Helvetica Neue", Arial, sans-serif;
  }
  .card__frame {
    position: absolute;
    left: 68px;
    top: 68px;
    width: 1062px;
    height: 544px;
    border: 7px solid var(--espresso);
    border-radius: 4px;
  }
  .brand {
    position: absolute;
    left: 0;
    top: 100px;
    width: 1200px;
    text-align: center;
  }
  .brand__dot {
    display: block;
    width: 92px;
    height: 92px;
    margin: 0 auto;
    border-radius: 50%;
    background: var(--roast);
  }
  .brand__name {
    display: block;
    margin-top: 6px;
    font-size: 84px;
    line-height: 96px;
    font-weight: 400;
    color: var(--espresso);
  }
  .brand__descriptor {
    display: block;
    margin-top: 8px;
    font-size: 18px;
    letter-spacing: 3px;
    color: var(--roast);
  }
  .slogan {
    position: absolute;
    left: 0;
    top: 352px;
    width: 1200px;
    text-align: center;
    font-size: 35px;
    line-height: 44px;
    color: var(--espresso);
  }
  .offerings {
    position: absolute;
    left: 128px;
    top: 408px;
    list-style: none;
    font-size: 29px;
    line-height: 39.5px;
    color: var(--roast);
  }
</style>
</head>
<body>
  <main class="card">
    <div class="card__frame"></div>

    <header class="brand">
      <span class="brand__dot"></span>
      <span class="brand__name">Tidy-Kettle</span>
      <span class="brand__descriptor">ORGANIC COFFEE + CAFE</span>
    </header>

    <p class="slogan">"Eat &amp; Drink Well, on the run!"</p>

    <ul class="offerings">
      <li>-Organic coffee, espresso &amp; tea</li>
      <li>-Blendora smoothies &amp; protein shakes</li>
      <li>-Zesty Pour (100% fresh local fruit and veggies)</li>
      <li>-Tender Nibs</li>
    </ul>
  </main>
</body>
</html>
```